I need creative and unique business card design using my company logo. Ok to change logo color. We are a small brokerage doing both Real Estate and Mortgage services. Need to have the follow on business card;
1. agent name - Mila Fenton - Realtor
2. cell - 949-555-0182
3. license number - DRE 04917362
4. business name - Brightway Estates & Lending, Inc
5. business office - 626-555-0147
6. business address - 287 W. Larkmoor Ave #214, Arcadia CA 91088
7. business logo - attached (ok to use different color on logo)

```html
<!DOCTYPE html>
<html lang="en">
<head>
<meta charset="UTF-8">
<title>Brightway Estates &amp; Lending – Business Card</title>
<link rel="stylesheet" href="https://fonts.googleapis.com/css2?family=Lato:wght@400;700&family=Montserrat:wght@800&display=swap">
<style>
  :root {
    --backdrop-top: #3a3c40;
    --backdrop-bottom: #1c1d20;
    --card-white: #ffffff;
    --brand-navy: #1a46a8;
    --brand-blue: #2a62c4;
    --brand-sky: #4aa3e6;
    --text-grey: #555a63;
    --rule-grey: #9aa0a8;
    --back-light: #3f86d4;
    --back-dark: #1d4ea8;
  }
  * { margin: 0; padding: 0; box-sizing: border-box; }
  html, body { width: 1200px; height: 952px; overflow: hidden; }
  body {
    background: linear-gradient(160deg, var(--backdrop-top), var(--backdrop-bottom));
    font-family: "Lato", Arial, sans-serif;
    display: flex;
    flex-direction: column;
    align-items: center;
    justify-content: center;
    gap: 56px;
  }
  .card {
    position: relative;
    width: 620px;
    height: 354px;
    border-radius: 22px;
    overflow: hidden;
    box-shadow: 0 14px 30px rgba(0,0,0,0.45);
  }
  /* bottom rule: light then dark segment */
  .card-rule {
    position: absolute;
    left: 0; right: 0;
    bottom: 34px;
    height: 8px;
  }
  .card-rule .rule-light {
    position: absolute; left: 0; width: 54%; bottom: 2px; height: 3px;
    background: var(--brand-sky);
  }
  .card-rule .rule-dark {
    position: absolute; left: 54%; right: 0; bottom: 0; height: 6px;
    background: var(--brand-navy);
  }

  /* front */
  .card-front { background: var(--card-white); }
  .brand-lockup {
    position: absolute;
    left: 40px; top: 70px;
    width: 250px;
    display: flex;
    flex-direction: column;
    align-items: center;
    color: var(--brand-blue);
    font-weight: 400;
  }
  .brand-mark {
    width: 82px; height: 82px;
    background: var(--brand-blue);
    margin-bottom: 14px;
  }
  .brand-name {
    font-size: 28px;
    letter-spacing: 7px;
    line-height: 1;
  }
  .brand-sub {
    margin-top: 8px;
    font-size: 10.5px;
    letter-spacing: 2.6px;
  }
  .agent {
    position: absolute;
    left: 330px; top: 62px;
    color: var(--text-grey);
  }
  .agent-name {
    font-family: "Montserrat", Arial, sans-serif;
    font-weight: 800;
    font-size: 27px;
    color: var(--brand-navy);
    letter-spacing: 0.5px;
    line-height: 1;
  }
  .agent-title { font-size: 15px; margin-top: 4px; }
  .agent-divider {
    width: 64px; height: 1px;
    background: var(--rule-grey);
    margin: 8px 0 12px;
  }
  .contact-list { list-style: none; font-size: 13.5px; line-height: 1.35; }
  .contact-list li { display: flex; gap: 8px; margin-bottom: 6px; }
  .contact-icon {
    flex: 0 0 16px; height: 16px; border-radius: 3px;
    background: var(--brand-blue);
    display: flex; align-items: center; justify-content: center;
    margin-top: 1px;
  }
  .license { font-size: 13.5px; margin-top: 2px; }

  /* back */
  .card-back {
    background: radial-gradient(ellipse at 45% 35%, var(--back-light), var(--back-dark) 75%);
  }
  .card-back .card-rule .rule-light { background: #5fb4f0; }
  .card-back .card-rule .rule-dark { background: #163f93; }
  .back-lockup {
    position: absolute;
    inset: 0;
    display: flex; flex-direction: column; align-items: center; justify-content: center;
    color: var(--card-white);
    font-weight: 400;
    padding-bottom: 20px;
  }
  .back-lockup .brand-mark { background: var(--card-white); width: 76px; height: 76px; }
</style>
</head>
<body>

  <section class="card card-front" aria-label="Business card front">
    <div class="brand-lockup">
      <div class="brand-mark"></div>
      <div class="brand-name">BRIGHTWAY</div>
      <div class="brand-sub">ESTATES &amp; LENDING, INC</div>
    </div>

    <div class="agent">
      <div class="agent-name">MILA FENTON</div>
      <div class="agent-title">Realtor</div>
      <div class="agent-divider"></div>
      <ul class="contact-list">
        <li>
          <span class="contact-icon">
            <svg width="10" height="12" viewBox="0 0 10 12"><path d="M5 0.5a4 4 0 0 0-4 4c0 3 4 7 4 7s4-4 4-7a4 4 0 0 0-4-4z" fill="#fff"/><circle cx="5" cy="4.5" r="1.5" fill="#2a62c4"/></svg>
          </span>
          <span>287 W. Larkmoor Ave #214,<br>Arcadia CA 91088</span>
        </li>
        <li>
          <span class="contact-icon">
            <svg width="8" height="12" viewBox="0 0 8 12"><rect x="0.8" y="0.8" width="6.4" height="10.4" rx="1.2" fill="none" stroke="#fff" stroke-width="1.4"/><circle cx="4" cy="9.2" r="0.8" fill="#fff"/></svg>
          </span>
          <span>949-555-0182</span>
        </li>
        <li>
          <span class="contact-icon">
            <svg width="11" height="11" viewBox="0 0 11 11"><path d="M2.2 0.8l1.8 2.2-1 1.2c.6 1.4 1.6 2.4 3 3l1.2-1 2.2 1.8-.9 1.8C5 9.6 1.4 6 1.2 1.7z" fill="#fff"/></svg>
          </span>
          <span>626-555-0147</span>
        </li>
      </ul>
      <div class="license">License Number - DRE 04917362</div>
    </div>

    <div class="card-rule"><span class="rule-light"></span><span class="rule-dark"></span></div>
  </section>

  <section class="card card-back" aria-label="Business card back">
    <div class="back-lockup">
      <div class="brand-mark"></div>
      <div class="brand-name">BRIGHTWAY</div>
      <div class="brand-sub">ESTATES &amp; LENDING, INC</div>
    </div>
    <div class="card-rule"><span class="rule-light"></span><span class="rule-dark"></span></div>
  </section>

</body>
</html>
```